Plumwick Inc. Website & Vexpad Apps Landing Pages

We need a web site design for our company. We develop software and do various consultant projects for our clients. Our products focus on the mobile platform, mainly the Vexpad (business, games, social, etc.). We want to communicate that our software is simple and good as candy. The web pages should be fun to look at not loosing seriousness and credibility. Web 2.0 style and 960 grid system a must. We are opened to any overall site colour scheme suggestions (look at the sites we like below).

Must haves:
- Our logo should be seen on the site and look great on it :-) (preview attached below)
- Main home page and app landing page.
- Section links/tabs on the home page (home,apps,support,blog,contact,about)
- No text in images
- Style sheet

Looks we like:
- http://k7r2mqx9tvbnwa.stashgrove.net/412_Zunder_Site/final_large.jpg
- http://k7r2mqx9tvbnwa.stashgrove.net/Select_81_Painterly_Vexpad_Landing_Page/final.jpg
- http://gruvlets.com/
- http://mondrake.ca/
- http://lumfold.com/

Industry/Entity Type

Business

Requirements
Must have
• - Company logo should look great on pages.
• - Main home page and app landing page.
• - Section links/tabs on the home page (home,apps,support,blog,contact,about)
• - Web 2.0 style.
• - 960 grid system (12 col, 16 col).
• - Sliced ann optmized
• - Exported in all major formats (psd,ai,eps,png,jpeg,etc)
• - Style sheet
Should not have
• - Text in images

```html
<!DOCTYPE html>
<html lang="en">
<head>
<meta charset="utf-8">
<title>Plumwick — Software simple and good as candy</title>
<link rel="stylesheet" href="https://fonts.googleapis.com/css2?family=Cabin:wght@400;500;600&family=Handlee&display=swap">
<style>
  :root {
    --wine-dark: #2a0d10;
    --wine: #5e1216;
    --wine-bright: #8a1a1c;
    --candy-red: #c8121f;
    --cream: #f3eec0;
    --paper: #f2f2f2;
    --tile-frame: #c9c9c9;
    --tile-fill: #666666;
    --ink: #222222;
    --muted-grey: #8a8a8a;
    --footer-bg: #2a1012;
    --footer-line: #3e1a1d;
    --white: #ffffff;
  }
  * { box-sizing: border-box; margin: 0; padding: 0; }
  html, body { width: 1133px; height: 1200px; overflow: hidden; }
  body {
    position: relative;
    background: var(--paper);
    font-family: "Cabin", sans-serif;
    color: var(--ink);
  }
  .hero {
    position: absolute; left: 0; top: 0; width: 1133px; height: 470px;
    background: linear-gradient(100deg, var(--wine-dark) 0%, var(--wine) 45%, var(--wine-bright) 80%, #7a1518 100%);
  }
  .brand {
    position: absolute; left: 44px; top: 20px;
    display: flex; align-items: center; gap: 10px;
    font-size: 42px; font-weight: 600; color: var(--white); letter-spacing: 0.5px;
  }
  .brand-dot { width: 30px; height: 30px; border-radius: 50%; background: var(--candy-red); }
  .main-nav { position: absolute; top: 37px; left: 0; width: 1133px; height: 20px; }
  .main-nav a {
    position: absolute; color: var(--white); text-decoration: none;
    font-size: 14px; letter-spacing: 0.5px; text-transform: uppercase;
  }
  .headline {
    position: absolute; left: 44px; top: 88px; width: 640px;
    font-size: 39px; font-weight: 500; line-height: 50px; color: #e6e6e6;
    text-shadow: 0 2px 2px rgba(0,0,0,.35);
  }
  .lede {
    position: absolute; left: 44px; top: 209px; width: 630px;
    font-size: 20px; line-height: 35.5px; color: var(--candy-red);
  }
  .lede .light { color: var(--cream); }
  .btn {
    position: absolute; top: 365px; width: 206px; height: 43px;
    border-radius: 4px; font-size: 16px; display: flex; align-items: center; justify-content: center;
    box-shadow: 0 2px 4px rgba(0,0,0,.35);
  }
  .btn-light { left: 44px; background: linear-gradient(#fafafa, #d6d6d6); color: var(--candy-red); border: 1px solid #bbb; }
  .btn-dark { left: 296px; background: linear-gradient(#4a4a4a, #2a2a2a); color: var(--cream); border: 1px solid #111; }
  .device-shot {
    position: absolute; left: 722px; top: 88px; width: 368px; height: 420px;
    border-radius: 26px;
    background: linear-gradient(160deg, #3a3a3a 0%, #9aa4ad 35%, #6f7a86 60%, #1a1a1a 100%);
    z-index: 3;
  }
  .edge { position: absolute; left: 0; width: 1133px; height: 14px; }
  .edge-hero { top: 452px; z-index: 2; }
  .edge-footer { top: 918px; z-index: 2; }
  .app-tile {
    position: absolute; width: 313px; height: 193px;
    border: 1px solid var(--tile-frame); border-radius: 5px; background: #f7f7f7; padding: 6px;
    overflow: hidden;
  }
  .app-tile .screen {
    width: 100%; height: 100%; border-radius: 5px; background: var(--tile-fill);
    display: flex; align-items: center; justify-content: center;
    color: var(--white); font-size: 17px;
  }
  .ribbon {
    position: absolute; right: -2px; top: -2px; width: 96px; height: 96px;
  }
  .customers-title { position: absolute; left: 733px; top: 538px; font-size: 17px; color: #333; }
  .client {
    position: absolute; font-size: 20px; font-weight: 600; color: var(--muted-grey);
  }
  .rule { position: absolute; left: 733px; top: 706px; width: 356px; height: 1px; background: #dcdcdc; }
  .testimonial {
    position: absolute; left: 740px; top: 731px; width: 352px;
    font-family: "Handlee", cursive; font-size: 13.5px; line-height: 22px; color: #333; letter-spacing: 0.4px;
  }
  .testimonial cite {
    display: block; text-align: right; margin-top: 15px; font-style: normal;
    font-family: "Cabin", sans-serif; font-weight: 600; font-size: 13px; color: #111;
  }
  .site-footer {
    position: absolute; left: 0; top: 930px; width: 1133px; height: 270px; background: var(--footer-bg);
  }
  .foot-heading { position: absolute; top: 27px; font-size: 15px; color: var(--candy-red); }
  .foot-line { position: absolute; top: 57px; height: 1px; background: var(--footer-line); }
  .foot-about { position: absolute; left: 44px; top: 73px; width: 440px; font-size: 12.5px; line-height: 19px; color: var(--cream); }
  .foot-about p + p { margin-top: 12px; }
  .foot-links { position: absolute; left: 673px; top: 73px; list-style: none; }
  .foot-links li { font-size: 13.5px; line-height: 26.5px; color: var(--white); }
  .social { position: absolute; left: 898px; font-size: 12.5px; color: var(--white); display: flex; align-items: center; gap: 22px; }
  .social .mark { width: 18px; height: 18px; border-radius: 3px; background: #6c93b8; }
  .social .accent { color: var(--candy-red); }
</style>
</head>
<body>
  <header class="hero">
    <div class="brand"><span class="brand-dot"></span>Plumwick</div>
    <nav class="main-nav">
      <a style="left:596px">Home</a>
      <a style="left:678px">Apps</a>
      <a style="left:753px">Support</a>
      <a style="left:857px">Blog</a>
      <a style="left:935px">Contact</a>
      <a style="left:1042px">About</a>
    </nav>
    <h1 class="headline">We make software simple and good as candy</h1>
    <p class="lede">Lorem ipsum <span class="light">dolor sit amet consectetur</span> adipiscing elit aenean vitae ullamcorper augue. <span class="light">Etiam mi lorem ultricies at dapibus</span> facilisis pharetra et diam.</p>
    <div class="btn btn-light">View our apps</div>
    <div class="btn btn-dark">Contact us</div>
  </header>

  <div class="device-shot" role="img" aria-label="Two Vexpad phones showing the home screen with app icons"></div>

  <svg class="edge edge-hero" viewBox="0 0 1133 14" preserveAspectRatio="none" aria-hidden="true">
    <defs>
      <pattern id="teeth-light" width="12" height="14" patternUnits="userSpaceOnUse">
        <polygon points="0,14 6,4 12,14" fill="#f2f2f2"/>
      </pattern>
    </defs>
    <rect width="1133" height="14" fill="url(#teeth-light)"/>
  </svg>

  <section class="apps">
    <div class="app-tile" style="left:44px;top:487px">
      <div class="screen">App 1</div>
      <svg class="ribbon" viewBox="0 0 96 96" aria-hidden="true">
        <polygon points="0,2 30,2 94,66 94,96" fill="#a8111b"/>
        <text x="58" y="40" fill="#fff" font-family="Cabin, sans-serif" font-size="15" transform="rotate(45 58 40)" text-anchor="middle">New</text>
      </svg>
    </div>
    <div class="app-tile" style="left:376px;top:487px"><div class="screen">App 2</div></div>
    <div class="app-tile" style="left:44px;top:703px"><div class="screen">App 3</div></div>
    <div class="app-tile" style="left:376px;top:703px"><div class="screen">App 4</div></div>
  </section>

  <aside>
    <h2 class="customers-title">Our costumers</h2>
    <span class="client" style="left:735px;top:588px">Norvale</span>
    <span class="client" style="left:882px;top:588px">Quillan</span>
    <span class="client" style="left:1024px;top:588px">Tessa</span>
    <span class="client" style="left:735px;top:650px">brightmoor</span>
    <span class="client" style="left:904px;top:650px">larkway</span>
    <span class="client" style="left:1034px;top:650px">Ovio</span>
    <div class="rule"></div>
    <blockquote class="testimonial">
      “Lorem ipsum dolor sit amet, consectetur adipig elit. Donec et nisi sem. Etiam at neque turpis, at ornare felis. Nullam vulputate vestibu lum sem eu suscipit. Sed faucibus con sectetur purus, sit amet suscipit sem luctus.”
      <cite>John Doe, Lorem ipsum Company</cite>
    </blockquote>
  </aside>

  <svg class="edge edge-footer" viewBox="0 0 1133 14" preserveAspectRatio="none" aria-hidden="true">
    <defs>
      <pattern id="teeth-dark" width="12" height="14" patternUnits="userSpaceOnUse">
        <polygon points="0,14 6,4 12,14" fill="#2a1012"/>
      </pattern>
    </defs>
    <rect width="1133" height="14" fill="url(#teeth-dark)"/>
  </svg>

  <footer class="site-footer">
    <h3 class="foot-heading" style="left:44px">About</h3>
    <div class="foot-line" style="left:44px;width:444px"></div>
    <div class="foot-about">
      <p>Maecenas vehicula venenatis faucibus. Nullam fermentum, velit vitae laoreet consequat, erat nisl hendrerit tellus, eu venenatis nunc odio id felis. Quisque leo ante, pulvinar vitae ultrices non, ornare vitae urna. In hac habitasse platea dictumst.</p>
      <p>Copyright © Plumwick 2010. All Rights Reserved</p>
    </div>
    <h3 class="foot-heading" style="left:673px">plumwick</h3>
    <div class="foot-line" style="left:673px;width:152px"></div>
    <ul class="foot-links">
      <li>Home</li><li>Apps</li><li>Suppport</li><li>Blog</li><li>Contact</li>
    </ul>
    <div class="social" style="top:32px"><span class="mark"></span><span>Follow us <span class="accent">on Chirpline</span></span></div>
    <div class="social" style="top:73px"><span class="mark"></span><span>Become a fan <span class="accent">on Gatherly</span></span></div>
  </footer>
</body>
</html>
```